Business Card Design

I need a business card design for a new company based in Sydney called 'The Brisk Ladle'. We deliver organic, gourmet and fine foods to your door.

I would like to see creative, unique designs which use colours which represent health and nature like green.

Target Market(s)

Health conscious 20 to 35 year olds.

Industry/Entity Type

Health

Contact Information for Business Card

The Brisk Ladle, Owen Pardalis, owen@thebriskladle.com.au, 0427865193

Requirements
Must have
• My logo.

```html
<!DOCTYPE html>
<html lang="en">
<head>
<meta charset="utf-8">
<title>The Brisk Ladle — Business Card</title>
<link rel="stylesheet" href="https://fonts.googleapis.com/css2?family=PT+Sans:wght@400;700&display=swap">
<style>
  :root {
    --backdrop-top: #e4e5e7;
    --backdrop-bottom: #c9cacd;
    --card: #ffffff;
    --card-edge: #eceded;
    --brand-green: #3f8a2e;
    --leaf-green: #8cc027;
    --deep-green: #2e7d32;
    --ink: #3a3a3a;
    --shadow: rgba(0, 0, 0, 0.18);
  }
  * { margin: 0; padding: 0; box-sizing: border-box; }
  html, body {
    width: 1200px;
    height: 800px;
    overflow: hidden;
  }
  body {
    background: linear-gradient(160deg, var(--backdrop-top), var(--backdrop-bottom));
    font-family: "PT Sans", sans-serif;
    color: var(--ink);
    display: flex;
    align-items: center;
    justify-content: center;
    gap: 60px;
  }
  .card {
    position: relative;
    width: 500px;
    height: 286px;
    background: var(--card);
    border: 1px solid var(--card-edge);
    box-shadow: 0 14px 30px var(--shadow);
    overflow: hidden;
  }
  .wordmark {
    display: flex;
    align-items: center;
    gap: 10px;
    color: var(--brand-green);
    font-weight: 400;
    font-size: 30px;
    line-height: 1;
    letter-spacing: 0.5px;
  }
  .wordmark-dot {
    width: 28px;
    height: 28px;
    border-radius: 50%;
    background: var(--leaf-green);
    flex-shrink: 0;
  }

  /* Back of card */
  .card-back {
    display: flex;
    flex-direction: column;
    align-items: center;
    justify-content: center;
    gap: 26px;
  }
  .card-back .website {
    font-size: 14px;
    letter-spacing: 0.3px;
  }

  /* Front of card */
  .card-front .wordmark {
    position: absolute;
    left: 40px;
    top: 40px;
    font-size: 26px;
  }
  .contact {
    position: absolute;
    left: 40px;
    top: 118px;
    font-size: 13px;
    line-height: 1.55;
  }
  .contact .person {
    color: var(--leaf-green);
    font-weight: 700;
    font-size: 16px;
    margin-bottom: 10px;
  }
  .contact .line {
    display: flex;
    align-items: center;
    gap: 8px;
  }
  .contact .line svg {
    width: 11px;
    height: 11px;
    flex-shrink: 0;
  }
  .contact .website {
    margin-top: 4px;
  }
  .accent-disc {
    position: absolute;
    right: -70px;
    bottom: -110px;
    width: 300px;
    height: 300px;
    border-radius: 50%;
    background: linear-gradient(135deg, var(--deep-green), var(--leaf-green));
  }
</style>
</head>
<body>

  <section class="card card-back" aria-label="Business card, back">
    <div class="wordmark"><span class="wordmark-dot"></span>The Brisk Ladle</div>
    <p class="website">www.thebriskladle.com.au</p>
  </section>

  <section class="card card-front" aria-label="Business card, front">
    <div class="wordmark"><span class="wordmark-dot"></span>The Brisk Ladle</div>

    <div class="contact">
      <p class="person">Owen Pardalis</p>
      <p class="line">
        <svg viewBox="0 0 12 12" aria-hidden="true">
          <rect x="3" y="0.5" width="6" height="11" rx="1.2" fill="none" stroke="var(--leaf-green)" stroke-width="1.3"/>
          <circle cx="6" cy="9.4" r="0.8" fill="var(--leaf-green)"/>
        </svg>
        owen@thebriskladle.com.au
      </p>
      <p class="line">
        <svg viewBox="0 0 12 12" aria-hidden="true">
          <rect x="0.5" y="2" width="11" height="8" rx="1" fill="var(--leaf-green)"/>
          <path d="M0.8 2.5 L6 6.6 L11.2 2.5" fill="none" stroke="#fff" stroke-width="1"/>
        </svg>
        0427865193
      </p>
      <p class="website">thebriskladle.com.au</p>
    </div>

    <div class="accent-disc"></div>
  </section>

</body>
</html>
```